Flyer for Golden Hearth Catering Company

Flyer Size: Double Sided 210mm * 148mm (Half a Sheet of Paper)
For your reference I have attached the logo and the web address is www.goldenhearthcatering.example.
Specifications:
- Must contain the menu pricing chart, contact information, and hours of operation posted on the website.
- The menu must have an organization system from 1. Select Glaze through 4.Drinks. This will be the determining factor for selection. Graphic must be a mixture of creativity and function.
-The flyer can be identical on both sides (Not a determining factor)
-Incorporate the logo on both sides.
-The flyer does not have to be based on the website. (Not a determining factor)
My team will be handing these flyers out to HR Directors and Securities at Corporate offices.
Please let me know if you have any questions.
Updates
Project Deadline Extended
Reason: Website was not operational .
Brief has been updated and the website is up for your reference.
Target Market(s)
Corporate Office Catering. Secretary or HR director, usually a female.
Industry/Entity Type
Catering
Look and feel
Each slider illustrates characteristics of the customer's brand and the style your logo design should communicate.

```html
<!DOCTYPE html>
<html lang="en">
<head>
<meta charset="utf-8">
<title>Golden Hearth Catering Company – Menu Flyer</title>
<link href="https://fonts.googleapis.com/css2?family=Tinos&family=Archivo+Black&display=swap" rel="stylesheet">
<style>
  :root {
    --bg: #3b2f08;
    --pattern: #8a7a4c;
    --heading: #f4f1e8;
    --body-ink: #0a0800;
    --ink-halo: rgba(200, 185, 140, 0.35);
    --brand: #ff3d12;
    --contact-ink: #000000;
  }
  html, body {
    margin: 0;
    padding: 0;
    width: 1200px;
    height: 845px;
    overflow: hidden;
    background: var(--bg);
  }
  .flyer {
    position: relative;
    width: 1200px;
    height: 845px;
    overflow: hidden;
    background: var(--bg);
    font-family: "Tinos", "Times New Roman", serif;
  }
  .pattern {
    position: absolute;
    inset: 0;
    background:
      radial-gradient(circle at 20% 30%, rgba(138,122,76,0.20), transparent 40%),
      radial-gradient(circle at 75% 60%, rgba(138,122,76,0.18), transparent 45%),
      radial-gradient(circle at 50% 85%, rgba(138,122,76,0.14), transparent 40%);
  }
  .section-title {
    position: absolute;
    margin: 0;
    font-weight: 400;
    font-size: 28px;
    line-height: 28px;
    color: var(--heading);
    white-space: nowrap;
  }
  .menu-list {
    position: absolute;
    margin: 0;
    padding: 0;
    list-style: none;
    font-size: 23.5px;
    line-height: 29px;
    color: var(--body-ink);
    text-shadow: 0 0 3px var(--ink-halo), 0 0 1px var(--ink-halo);
    white-space: nowrap;
  }
  .glaze-title { left: 82px; top: 103px; }
  .glaze-list { left: 82px; top: 161px; }
  .sides-title { left: 698px; top: 107px; }
  .sides-list { left: 699px; top: 170px; }
  .dessert-title { left: 460px; top: 491px; }
  .dessert-list { left: 319px; top: 521px; }
  .drinks-title { left: 465px; top: 594px; }
  .drinks-list { left: 323px; top: 624px; }

  .brand {
    position: absolute;
    left: 18px;
    top: 722px;
    display: flex;
    align-items: center;
    gap: 14px;
  }
  .brand-dot {
    width: 64px;
    height: 64px;
    border-radius: 50%;
    background: var(--brand);
  }
  .brand-name {
    font-family: "Tinos", "Times New Roman", serif;
    font-size: 30px;
    line-height: 1.05;
    color: var(--brand);
  }

  .contact {
    position: absolute;
    left: 698px;
    top: 738px;
    width: 495px;
    height: 90px;
    font-style: normal;
    font-family: "Archivo Black", "Arial Black", sans-serif;
    color: var(--contact-ink);
    font-size: 19px;
    line-height: 28px;
    text-transform: uppercase;
  }
  .contact-label { position: absolute; left: 205px; top: 0; margin: 0; font-size: 19px; font-weight: 400; }
  .contact-phone { position: absolute; left: 59px; top: 28px; white-space: nowrap; }
  .contact-email { position: absolute; left: 9px; top: 56px; white-space: nowrap; }
</style>
</head>
<body>
<main class="flyer">
  <div class="pattern" role="img" aria-label="Scattered pale chicken silhouettes across the background"></div>

  <h2 class="section-title glaze-title">1.SELECT ROTISSERIE CHICKEN GLAZE</h2>
  <ul class="menu-list glaze-list">
    <li>ORIGINAL</li>
    <li>BARBECUE</li>
    <li>HONEY</li>
    <li>SPICY</li>
    <li>CHIPOTLE</li>
    <li>CHIPOTLE-LIME</li>
    <li>JAMAICAN JERK</li>
    <li>TERIYAKI</li>
    <li>BUFFALO</li>
  </ul>

  <h2 class="section-title sides-title">2.SELECT SIDES</h2>
  <ul class="menu-list sides-list">
    <li>CAESAR SALAD</li>
    <li>FRIED RICE</li>
    <li>WHITE RICE</li>
    <li>MASHED POTATOES</li>
    <li>HUMMUS &amp; PITA</li>
  </ul>

  <h2 class="section-title dessert-title">3.SELECT DESSERT</h2>
  <ul class="menu-list dessert-list">
    <li>HAZELMOOR COVERED CHOCOLATE CHIP COOKIES</li>
  </ul>

  <h2 class="section-title drinks-title">4.SELECT DRINKS</h2>
  <ul class="menu-list drinks-list">
    <li>FIZZO COLA</li>
    <li>POPSA</li>
    <li>LEMMO LIME</li>
    <li>SUNMESA ICE TEA (ICED TEA &amp; LEMON TEA)</li>
    <li>PINE HOLLOW WATER</li>
  </ul>

  <div class="brand">
    <span class="brand-dot"></span>
    <span class="brand-name">Golden Hearth<br>Catering</span>
  </div>

  <address class="contact">
    <h3 class="contact-label">CONTACT US</h3>
    <div class="contact-phone">(555) 014-2290</div>
    <div class="contact-email">SALES@GOLDENHEARTHCATERING.EXAMPLE</div>
  </address>
</main>
</body>
</html>
```